High-end Packaging Design For Permanent Holiday Lights

We need a design for our product box for our company HaloSpan which sells permanent Christmas lights.
Box dimensions: 12.69 X 12.69 X 2.06
The box contains a starter kit and lights for customers who want to install their own permanent holiday lights. We want to see classy minimalistic designs the incorporate our logo and brand guidelines.

More white space and use of our logo.

Do not use random imagines of Christmas lights or weird shapes for the design.

This should mimic the style of an orvane zumrik packaging or high end laptop etc.

Target Market(s)

35+ men and women who love the holidays

Industry/Entity Type

Holiday lights

Font styles to use
Other font styles liked:
• Gotham

Requirements
Must have
• Must have our logo, must be classy/high end, must give multiple color options.
Nice to have
• Possible raised foil logo, or different ideas for our logo elements, play around with layouts for the box dimensions.
Should not have
• shouldn't contain any Christmas design elements as our product is used year round,

```html
<!DOCTYPE html>
<html lang="en">
<head>
<meta charset="utf-8">
<title>HaloSpan – Permanent Lights Box</title>
<link rel="stylesheet" href="https://fonts.googleapis.com/css2?family=Bebas+Neue&family=Barlow+Condensed:wght@500&family=Montserrat:wght@500&display=swap">
<style>
  :root {
    --page-bg: #eeeeee;
    --box-deep: #1d0838;
    --box-mid: #3a0f66;
    --side-deep: #170630;
    --ribbon-gold: #e5a923;
    --ribbon-blue: #1d5fe0;
    --accent-pink: #ee2f86;
    --pill-navy: #0a0e5c;
    --pill-blue: #1836d8;
    --mark-violet: #8e3fe6;
    --text-white: #ffffff;
  }
  * { margin: 0; padding: 0; box-sizing: border-box; }
  html, body {
    width: 1200px; height: 944px; overflow: hidden;
    background: var(--page-bg);
  }
  .canvas {
    position: relative; width: 1200px; height: 944px;
    display: flex; align-items: center; justify-content: center;
  }
  .box {
    display: flex; height: 760px;
  }
  .box-side {
    position: relative; width: 140px; height: 100%; overflow: hidden;
    background: var(--side-deep);
  }
  .box-side .light-art {
    background:
      radial-gradient(ellipse 120% 14% at 80% 40%, rgba(155,60,240,.45), transparent 70%),
      radial-gradient(ellipse 120% 16% at 70% 82%, rgba(224,79,208,.4), transparent 70%),
      linear-gradient(180deg, var(--side-deep), #27094a 50%, var(--side-deep));
  }
  .side-label {
    position: absolute; top: 74px; right: 28px;
    writing-mode: vertical-rl;
    font-family: "Bebas Neue", sans-serif; font-size: 40px; line-height: 1.25;
    color: var(--text-white);
  }
  .box-front {
    position: relative; width: 590px; height: 100%; overflow: hidden;
    background: var(--box-deep);
  }
  .light-art {
    position: absolute; inset: 0;
  }
  .box-front .light-art {
    background:
      radial-gradient(ellipse 70% 22% at 55% 20%, rgba(155,60,240,.55), transparent 70%),
      radial-gradient(ellipse 80% 20% at 45% 85%, rgba(224,79,208,.45), transparent 70%),
      radial-gradient(ellipse 60% 12% at 60% 90%, rgba(217,195,90,.25), transparent 70%),
      radial-gradient(ellipse 90% 60% at 50% 50%, var(--box-mid), var(--box-deep));
  }
  .length-ribbon {
    position: absolute; top: 0; right: 24px; width: 94px; height: 153px;
    background: var(--ribbon-gold);
    clip-path: polygon(0 0, 100% 0, 100% 100%, 50% 88%, 0 100%);
    display: flex; justify-content: center; padding-top: 78px;
  }
  .length-ribbon__value {
    font-family: "Bebas Neue", sans-serif; font-size: 46px; line-height: 1;
    color: var(--ribbon-blue);
  }
  .feature-tag {
    position: absolute; top: 155px; right: 20px; width: 102px;
    font-family: "Bebas Neue", sans-serif; font-size: 32px; line-height: 1.1;
    color: var(--accent-pink); text-align: center;
  }
  .brand-mark {
    position: absolute; top: 262px; left: 237px; width: 116px; height: 116px;
    border-radius: 50%; background: var(--mark-violet);
  }
  .brand-name {
    position: absolute; top: 416px; left: 0; right: 0; text-align: center;
    font-family: "Montserrat", sans-serif; font-weight: 500; font-size: 50px;
    letter-spacing: 8px; color: var(--text-white); line-height: 1.2;
  }
  .product-pill {
    position: absolute; top: 495px; left: 63px; width: 468px; height: 56px;
    border-radius: 28px;
    background: linear-gradient(90deg, var(--pill-navy) 0%, var(--pill-blue) 55%, var(--pill-navy) 100%);
    display: flex; align-items: center; justify-content: center;
    font-family: "Barlow Condensed", sans-serif; font-weight: 500; font-size: 28px;
    color: var(--text-white); letter-spacing: .3px;
  }
  .spec-label {
    position: absolute; right: 30px; top: 620px; text-align: right;
    font-family: "Bebas Neue", sans-serif; font-size: 38px; line-height: 1.22;
    color: var(--text-white);
    text-shadow: 0 2px 4px rgba(0,0,0,.45);
  }
</style>
</head>
<body>
<main class="canvas">
  <div class="box">
    <section class="box-side">
      <div class="light-art" role="img" aria-label="Violet and magenta light streaks continuing across a dark purple side panel"></div>
      <p class="side-label">LED STRIP LIGHT<br>24.6FTX2</p>
    </section>

    <section class="box-front">
      <div class="light-art" role="img" aria-label="Sweeping ribbons of violet, magenta and gold light streaks orbiting across a dark purple background"></div>

      <div class="length-ribbon"><span class="length-ribbon__value">50FT</span></div>
      <p class="feature-tag">COLOR CHANGING</p>

      <div class="brand-mark" aria-hidden="true"></div>
      <h1 class="brand-name">HALOSPAN</h1>
      <p class="product-pill">PERMANENT CHRISTMAS LIGHTS</p>

      <p class="spec-label">LED STRIP LIGHT<br>24.6FTX2</p>
    </section>
  </div>
</main>
</body>
</html>
```